Verpackungskartons
Zielgruppe
Wir, die Firma kostWanne (www.kostwanne.de) suchen für unsere beiden Verpackungskartons (klein ca. 14x14x17 groß ca. 18x18x26) ein neues Design, wobei beide Kartons mit dem selben Design auskommen sollen. Beide Kartons sind auf allen Seiten geschlossen (kein Sichtfenster)
Unsere Sets werden vor allem als Geschenk von allen Altersgruppen gekauft.
Aufgabenstellung
- Vorderseite mit Logo

```html
<!DOCTYPE html>
<html lang="de">
<head>
<meta charset="utf-8">
<title>kostWanne – Verpackungskarton Stanzform</title>
<link rel="stylesheet" href="https://fonts.googleapis.com/css2?family=Quicksand:wght@300;400;600&display=swap">
<style>
  :root {
    --paper: #ececec;
    --navy: #1a1f3d;
    --wood-dark: #2e211b;
    --wood-mid: #4a3529;
    --wood-light: #5d4333;
    --steel: #b9bbbb;
    --steel-light: #d8d9d9;
    --white: #ffffff;
  }
  * { box-sizing: border-box; margin: 0; padding: 0; }
  html, body { width: 1200px; height: 929px; overflow: hidden; background: var(--paper); }
  .net { position: relative; width: 1200px; height: 929px; font-family: "Quicksand", sans-serif; }
  .part { position: absolute; }
  .wood-v { background: linear-gradient(90deg, var(--wood-dark), var(--wood-mid) 30%, var(--wood-dark) 55%, var(--wood-light) 80%, var(--wood-dark)); }
  .wood-h { background: linear-gradient(180deg, var(--wood-dark), var(--wood-mid) 30%, var(--wood-dark) 55%, var(--wood-light) 80%, var(--wood-dark)); }
  .steel-h { background: linear-gradient(180deg, var(--steel), var(--steel-light) 50%, var(--steel)); }
  .steel-v { background: linear-gradient(90deg, var(--steel), var(--steel-light) 50%, var(--steel)); }
  .band { background: var(--navy); color: var(--white); display: flex; align-items: center; justify-content: center; }
  .url { font-size: 14px; font-weight: 400; letter-spacing: 0.3px; }
  .flip { transform: rotate(180deg); }
  .brand { position: absolute; display: flex; align-items: center; gap: 16px; white-space: nowrap; }
  .brand .mark { width: 70px; height: 70px; border: 3px solid var(--white); border-radius: 50%; }
  .brand .name { font-size: 26px; font-weight: 400; color: var(--white); }
  .brand-left { left: 146px; top: 466px; transform: translate(-50%, -50%) rotate(-90deg); }
  .brand-right { left: 782px; top: 466px; transform: translate(-50%, -50%) rotate(90deg); flex-direction: row-reverse; }
  .logo-slot { position: absolute; left: 1064px; top: 464px; width: 186px; height: 186px; transform: translate(-50%, -50%);
    border: 6px solid var(--white); border-radius: 50%; display: flex; align-items: center; justify-content: center; }
  .logo-slot span { color: var(--white); font-weight: 600; font-size: 28px; line-height: 1.05; text-align: center; transform: rotate(-12deg); }
</style>
</head>
<body>
<main class="net">
  <!-- top flap -->
  <div class="part wood-v" style="left:329px;top:0;width:271px;height:65px" role="img" aria-label="Dunkle Holzdielen-Textur"></div>
  <div class="part steel-h" style="left:329px;top:65px;width:271px;height:8px"></div>
  <div class="part band" style="left:329px;top:73px;width:271px;height:147px"><span class="url">kostWanne.de</span></div>
  <div class="part steel-h" style="left:329px;top:220px;width:271px;height:8px"></div>
  <div class="part wood-v" style="left:329px;top:228px;width:271px;height:101px" role="img" aria-label="Dunkle Holzdielen-Textur"></div>

  <!-- left side -->
  <div class="part wood-h" style="left:0;top:329px;width:65px;height:271px" role="img" aria-label="Dunkle Holzdielen-Textur"></div>
  <div class="part steel-v" style="left:65px;top:329px;width:8px;height:271px"></div>
  <div class="part band" style="left:73px;top:329px;width:147px;height:271px"></div>
  <div class="part steel-v" style="left:220px;top:329px;width:8px;height:271px"></div>
  <div class="part wood-h" style="left:228px;top:329px;width:101px;height:271px" role="img" aria-label="Dunkle Holzdielen-Textur"></div>
  <div class="brand brand-left"><span class="mark"></span><span class="name">kostWanne</span></div>

  <!-- centre panel -->
  <div class="part wood-v" style="left:329px;top:329px;width:271px;height:271px" role="img" aria-label="Dunkle Holzdielen-Textur"></div>

  <!-- right side -->
  <div class="part wood-h" style="left:600px;top:329px;width:101px;height:271px" role="img" aria-label="Dunkle Holzdielen-Textur"></div>
  <div class="part steel-v" style="left:701px;top:329px;width:8px;height:271px"></div>
  <div class="part band" style="left:709px;top:329px;width:147px;height:271px"></div>
  <div class="part steel-v" style="left:856px;top:329px;width:8px;height:271px"></div>
  <div class="part wood-h" style="left:864px;top:329px;width:64px;height:271px" role="img" aria-label="Dunkle Holzdielen-Textur"></div>
  <div class="brand brand-right"><span class="mark"></span><span class="name">kostWanne</span></div>

  <!-- front face -->
  <div class="part wood-v" style="left:928px;top:329px;width:272px;height:271px" role="img" aria-label="Dunkle Holzdielen-Textur"></div>
  <div class="logo-slot"><span>IHR<br>LOGO</span></div>

  <!-- bottom flap -->
  <div class="part wood-v" style="left:329px;top:600px;width:271px;height:101px" role="img" aria-label="Dunkle Holzdielen-Textur"></div>
  <div class="part steel-h" style="left:329px;top:701px;width:271px;height:8px"></div>
  <div class="part band" style="left:329px;top:709px;width:271px;height:147px"><span class="url flip">kostWanne.de</span></div>
  <div class="part steel-h" style="left:329px;top:856px;width:271px;height:8px"></div>
  <div class="part wood-v" style="left:329px;top:864px;width:271px;height:65px" role="img" aria-label="Dunkle Holzdielen-Textur"></div>
</main>
</body>
</html>
```